Need help in designing new business card utilizing our new logo.

BuildMarq Solutions works with Construction Business Owners, Managers & IT Professionals to strengthen software usage and increase user productivity.

Our Construction Accounting and Mobile Field Management Software Clients engage with us in the following areas:

New Software Implementations
Software Re-Implementations
Redesigning Software Usage at the User Level
Project Coordination & Management
Continued Software Support

Old tag line:
Clear Choices - Working Systems That Last

www.buildmarq-solutions.example

Stride 4 is a product, but not needed for a new business card.

```html
<!DOCTYPE html>
<html lang="en">
<head>
<meta charset="utf-8">
<title>BuildMarq Solutions – Business Card</title>
<link rel="stylesheet" href="https://fonts.googleapis.com/css2?family=Raleway:ital,wght@0,300;0,400;0,500;0,600;1,300&display=swap">
<style>
  :root {
    --backdrop: #F8B23E;
    --card: #FFFFFF;
    --brand-blue: #2B3A93;
    --brand-grey: #C6C7C9;
    --text-grey: #5C5F66;
    --muted-grey: #B4B6BA;
  }
  * { box-sizing: border-box; margin: 0; padding: 0; }
  html, body {
    width: 1200px; height: 1145px; overflow: hidden;
    background: var(--backdrop);
    font-family: "Raleway", sans-serif;
  }
  .canvas { position: relative; width: 1200px; height: 1145px; }

  .card {
    position: absolute; left: 248px; width: 677px; height: 394px;
    background: var(--card);
    overflow: hidden;
  }
  .card--front { top: 96px; }
  .card--back { top: 641px; }

  /* front */
  .wordmark {
    position: absolute; left: 50px; top: 54px;
    display: flex; align-items: center; gap: 12px;
  }
  .wordmark__square { width: 40px; height: 40px; background: var(--brand-blue); }
  .wordmark__name {
    font-weight: 600; font-size: 34px; letter-spacing: 1px;
    color: var(--brand-blue); line-height: 1;
  }
  .tagline {
    position: absolute; left: 50px; top: 124px;
    font-size: 12px; color: var(--text-grey); letter-spacing: .2px;
  }
  .person__name {
    position: absolute; left: 50px; top: 176px;
    font-size: 34px; font-weight: 500; color: var(--brand-blue);
  }
  .person__title {
    position: absolute; left: 50px; top: 220px;
    font-size: 23px; font-weight: 300; font-style: italic; color: var(--muted-grey);
  }
  .contacts {
    position: absolute; left: 50px; top: 276px; list-style: none;
  }
  .contacts li {
    display: flex; align-items: center; gap: 9px;
    font-size: 16px; color: var(--text-grey); height: 26px;
  }
  .contacts svg { width: 14px; height: 14px; fill: var(--brand-blue); flex: none; }

  .brand-decoration {
    position: absolute; right: 0; top: 0; width: 250px; height: 394px;
    background: linear-gradient(160deg, var(--brand-blue) 0%, #7F88B8 50%, var(--brand-grey) 100%);
  }

  /* back */
  .back-decoration {
    position: absolute; left: 0; top: 33px; width: 104px; height: 311px;
    background: linear-gradient(180deg, var(--brand-blue) 0%, #8A91BC 45%, var(--brand-grey) 100%);
  }
  .services {
    position: absolute; left: 187px; top: 64px; list-style: none;
  }
  .services li {
    position: relative; padding-left: 28px;
    font-size: 23px; color: var(--text-grey); line-height: 44px;
  }
  .services li::before {
    content: ""; position: absolute; left: 0; top: 16px;
    width: 13px; height: 13px; background: var(--brand-blue);
  }
  .services .continued::before { display: none; }
</style>
</head>
<body>
<div class="canvas">

  <section class="card card--front" aria-label="Business card front">
    <div class="wordmark">
      <span class="wordmark__square"></span>
      <span class="wordmark__name">BUILDMARQ</span>
    </div>
    <p class="tagline">Clear Choices - Working Systems That Last</p>

    <h1 class="person__name">Dana R. Whitfield</h1>
    <p class="person__title">Owner</p>

    <ul class="contacts">
      <li>
        <svg viewBox="0 0 24 24" aria-hidden="true"><path d="M6.6 10.8a15.1 15.1 0 0 0 6.6 6.6l2.2-2.2c.3-.3.7-.4 1-.2 1.1.4 2.3.6 3.6.6.6 0 1 .4 1 1V20c0 .6-.4 1-1 1A17 17 0 0 1 3 4c0-.6.4-1 1-1h3.5c.6 0 1 .4 1 1 0 1.3.2 2.5.6 3.6.1.3 0 .7-.2 1z"/></svg>
        800-555-0142 ext 100
      </li>
      <li>
        <svg viewBox="0 0 24 24" aria-hidden="true"><circle cx="12" cy="12" r="10"/></svg>
        518-555-0193
      </li>
      <li>
        <svg viewBox="0 0 24 24" aria-hidden="true"><path d="M2 5h20v14H2zm2 2v.5l8 5 8-5V7z"/></svg>
        dana.whitfield@buildmarq.example
      </li>
    </ul>

    <div class="brand-decoration" role="img" aria-label="Large brand mark decoration area"></div>
  </section>

  <section class="card card--back" aria-label="Business card back">
    <div class="back-decoration" role="img" aria-label="Brand motif decoration area"></div>

    <ul class="services">
      <li>New Software Implementations</li>
      <li>Software Re-Implementations</li>
      <li>Project Coordination &amp; Management</li>
      <li>Continued Software Support</li>
      <li>Redesigning Software Usage at the</li>
      <li class="continued">User Level</li>
    </ul>
  </section>

</div>
</body>
</html>
```